Create a flyer for our party getaway to Ibiza.

'The Crimson Ibiza Escape'

Friday 14th July - Monday 17th July

DJ Morvek & DJ Tundral brings together a jam-packed weekend schedule full of the best urban parties in Ibiza.

What's included?

4 Nights Of Entertainment
6 Parties In Total
1 Boat Party
1 Pool Party
2 Superclub Parties
1 Indoor Water Party
Bottomless Drinks (Boat Party Only)
An unbelievable experience
1 unbeatable price.

All this for 140€ (you save 50€ when you book with us)

Tickets avaialble from Ticketlane & Gribolo

Target Market(s)

holiday goers

Industry/Entity Type

party, events, club, hip hop

Requirements
Must have
• good vibes
Nice to have
• nice catchy looking title

```html
<!DOCTYPE html>
<html lang="en">
<head>
<meta charset="utf-8">
<title>The Crimson Ibiza Escape</title>
<link rel="stylesheet" href="https://fonts.googleapis.com/css2?family=Alfa+Slab+One&family=Audiowide&family=Barlow:wght@500&family=Kaushan+Script&family=Montserrat:wght@300;600;700;800&family=Archivo+Black&display=swap">
<style>
  :root {
    --outer-top: #0b0624;
    --outer-bottom: #2b0f4e;
    --poster-top: #14207a;
    --poster-mid: #1c2a92;
    --poster-bottom: #3a1470;
    --panel: #4a0a5e;
    --yellow: #f6e600;
    --gold: #f7c21a;
    --orange: #f79a14;
    --magenta: #ff2bd6;
    --white: #ffffff;
    --ink: #14123a;
  }
  * { margin: 0; padding: 0; box-sizing: border-box; }
  html, body { width: 848px; height: 1200px; overflow: hidden; }
  body {
    position: relative;
    background: linear-gradient(180deg, var(--outer-top), var(--outer-bottom));
    font-family: "Montserrat", sans-serif;
    color: var(--white);
  }
  .poster {
    position: absolute; left: 36px; top: 50px; width: 777px; height: 1100px;
    background: linear-gradient(180deg, var(--poster-top) 0%, var(--poster-mid) 40%, var(--poster-bottom) 100%);
    overflow: hidden;
  }
  .crowd {
    position: absolute; left: 0; right: 0; bottom: 0; height: 230px;
    background: linear-gradient(180deg, rgba(60,20,110,0) 0%, rgba(70,25,120,.55) 60%, rgba(60,18,105,.7) 100%);
  }
  .title-main {
    position: absolute; left: 0; right: 0; top: 80px; text-align: center;
    font-family: "Alfa Slab One", serif; font-size: 54px; line-height: 1;
    letter-spacing: .5px;
  }
  .title-accent {
    position: absolute; left: 0; right: 0; top: 152px; text-align: center;
    font-family: "Audiowide", sans-serif; font-size: 68px; line-height: 1;
    color: var(--yellow); letter-spacing: 2px;
    text-shadow: 4px 4px 0 var(--magenta);
  }
  .triangle { position: absolute; left: 0; top: 0; width: 777px; height: 1100px; }
  .hosts-photo {
    position: absolute; left: 70px; top: 195px; width: 560px; height: 345px;
    border-radius: 40% 40% 6px 6px / 30% 30% 6px 6px;
    background: radial-gradient(ellipse at 50% 45%, #e9e6f2 0%, #b9a6d8 35%, #5a4aa8 70%, rgba(28,42,146,0) 100%);
  }
  .dates {
    position: absolute; left: 0; right: 0; top: 536px; text-align: center;
    font-family: "Barlow", sans-serif; font-weight: 500; font-size: 35px; line-height: 1.2;
    text-shadow: 0 2px 6px rgba(0,0,0,.4);
  }
  .dates sup { font-size: 18px; vertical-align: 16px; }
  .panel {
    position: absolute; left: 54px; top: 633px; width: 668px; height: 253px;
    background: var(--panel); border-radius: 16px;
  }
  .panel-heading {
    position: absolute; left: 0; right: 0; top: 590px; text-align: center;
    font-family: "Kaushan Script", cursive; font-size: 56px; line-height: 1.1;
    text-shadow: -2px -2px 0 #000, 2px -2px 0 #000, -2px 2px 0 #000, 2px 2px 0 #000, 3px 4px 0 #000;
  }
  .item { position: absolute; display: flex; align-items: center; gap: 8px; }
  .item-number {
    font-family: "Montserrat", sans-serif; font-weight: 700; font-size: 44px;
    color: var(--gold); line-height: 1;
  }
  .item-label { font-weight: 700; font-size: 17px; line-height: 1.15; }
  .extra { position: absolute; font-weight: 700; font-size: 16px; line-height: 1.2; }
  .offer-intro {
    position: absolute; left: 92px; width: 192px; top: 928px; text-align: center;
    font-weight: 700; font-size: 18px;
  }
  .price {
    position: absolute; left: 92px; top: 957px; width: 192px; height: 63px;
    border-radius: 30px;
    background: linear-gradient(180deg, #ffd21f 0%, var(--orange) 100%);
    color: var(--ink); font-family: "Archivo Black", sans-serif; font-size: 48px;
    display: flex; align-items: center; justify-content: center; letter-spacing: -1px;
  }
  .saving {
    position: absolute; left: 72px; width: 232px; top: 1030px; text-align: center;
    font-weight: 700; font-size: 13px; line-height: 1.2;
  }
  .saving b { color: var(--gold); }
  .seller {
    position: absolute; top: 942px; font-weight: 700; font-size: 26px; line-height: 1.2;
  }
  .tickets {
    position: absolute; left: 410px; width: 240px; top: 1004px; text-align: center;
    font-size: 19px; line-height: 1.55;
  }
  .tickets .light { font-weight: 300; letter-spacing: .5px; }
  .tickets .bold { font-weight: 700; font-size: 20px; }
</style>
</head>
<body>
  <main class="poster">
    <div class="crowd" role="img" aria-label="Silhouettes of a dancing party crowd with raised hands"></div>

    <svg class="triangle" viewBox="0 0 777 1100" aria-hidden="true">
      <polygon points="63,410 643,284 544,600" fill="none" stroke="#f2e21a" stroke-width="22" stroke-linejoin="miter" opacity=".85"/>
    </svg>

    <div class="hosts-photo" role="img" aria-label="Photo of the two hosting DJs, DJ Morvek and DJ Tundral, posing in white t-shirts at the decks"></div>

    <h1 class="title-main">The Crimson Ibiza</h1>
    <div class="title-accent">ESCAPE</div>

    <p class="dates">Friday 14<sup>th</sup> July - Monday 17<sup>th</sup> July</p>

    <section class="panel" aria-labelledby="included"></section>
    <h2 class="panel-heading" id="included">Whats included?</h2>

    <div class="item" style="left:120px; top:692px;"><span class="item-number">4</span><span class="item-label">Nights Of<br>Entertainment</span></div>
    <div class="item" style="left:350px; top:692px;"><span class="item-number">1</span><span class="item-label">Pool<br>Party</span></div>
    <div class="item" style="left:519px; top:692px;"><span class="item-number">6</span><span class="item-label">Parties in<br>Total</span></div>

    <div class="item" style="left:120px; top:757px;"><span class="item-number">2</span><span class="item-label">Superclub<br>Parties</span></div>
    <div class="item" style="left:350px; top:757px;"><span class="item-number">1</span><span class="item-label">Boat<br>Party</span></div>
    <div class="item" style="left:519px; top:757px;"><span class="item-number">2</span><span class="item-label">Indoor<br>Water Party</span></div>

    <p class="extra" style="left:118px; top:827px;">Bottomless Drinks<br>(Boat Party Only)</p>
    <p class="extra" style="left:351px; top:827px;">An unbelievable<br>experience</p>
    <p class="extra" style="left:519px; top:846px;">1 unbeatable price</p>

    <p class="offer-intro">ALL THIS FOR</p>
    <div class="price">140€</div>
    <p class="saving">YOU SAVE <b>50€</b> WHEN<br>YOU BOOK WITH US</p>

    <span class="seller" style="left:375px;">Ticketlane</span>
    <span class="seller" style="left:545px;">Gribolo</span>

    <p class="tickets"><span class="light">Tickets avaialble from</span><br><span class="bold">Ticketlane &amp; Gribolo</span></p>
  </main>
</body>
</html>
```